ESPDT Flyer to promote our services in the PVT Event in Nashville, TN

Please use our website at www.sunnysprout-kids.com to get our color seem and details about our program to design a flyer. This is exclusively for our EPSDT service not clinics or optometry.
SSI Mission Statement
Larkfield Holdings, LLC, dba, "Sunny Sprout" feels a strong sense of connection to entities whose mission is to improve the educational achievements of students. In a similar way, Sunny Sprout is committed to improving the health of children by providing healthcare to students and in a school-based setting. We work to keep children healthy, ready to learn and in the classroom.
We believe that undiagnosed and untreated health problems can become barriers to a child's ability to learn. We believe that preventive health services, in the school setting, reduce or eliminate barriers to healthcare. We believe that diversity is to be valued and respected.
It is Sunny Sprout's desire provide the Annual health exams / Sports physicals and Optometry services to your students.
Description of Services
Annual Health Screening
These annual screenings and sports physicals will comply with the Early Periodic Screening, Diagnosis and Treatment (EPSDT) as mandated by the Tennessee Medicaid program. The intent of the EPSDT program is to identify problems at birth (Early), to check health status at different intervals (Periodic), provide services that will identify health issues (Screening) that lead to classification of health issues (Diagnosis and follow-up), and elimination or provide ongoing care for diagnosed health problems (Treatment).
Sunny Sprout transports a portable and well-equipped clinic to each school site. Sunny Sprout's practitioners diagnose medical illnesses and make referrals to the child’s primary care provider (PCP). The clinical teams consist of a Nurse Practitioner and three support team members.
This service is at No out-of-pocket Cost to the school district or parent. We bill insurances.
Target Market(s)
Coordinated School Healthcare Professinals
Industry/Entity Type
Health And Wellness
Requirements
Must have
- Must have description of the EPSDT exam
Nice to have
- Picture of diversity: Children and Nurses

```html
<!DOCTYPE html>
<html lang="en">
<head>
<meta charset="utf-8">
<title>Sunny Sprout – School Health Services Executive Summary</title>
<link rel="stylesheet" href="https://fonts.googleapis.com/css2?family=Cinzel:wght@400;600&family=Crimson+Text:ital,wght@0,600;1,400&family=Open+Sans:wght@400;600&display=swap">
<style>
  :root {
    --brand-blue: #0f5fae;
    --deep-blue: #0b4f97;
    --sky-blue: #5cbde8;
    --pale-blue: #cfe9f7;
    --accent-blue: #3aa6df;
    --footer-text: #5fb9e9;
    --body-text: #3a3a3a;
    --white: #ffffff;
  }
  * { box-sizing: border-box; margin: 0; padding: 0; }
  html, body {
    width: 1004px; height: 1200px; overflow: hidden;
    background: var(--white);
    font-family: "Open Sans", Arial, sans-serif;
  }
  .flyer {
    position: absolute; left: 59px; top: 28px;
    width: 877px; height: 1143px;
    border: 2px solid var(--brand-blue);
    background: var(--white);
    overflow: hidden;
  }
  .header {
    position: absolute; left: 0; top: 0; width: 100%; height: 242px;
    background: var(--brand-blue);
  }
  .header-curve { position: absolute; left: 0; top: 0; }
  .brand {
    position: absolute; left: 54px; top: 34px;
    display: flex; align-items: center; gap: 12px;
  }
  .brand-dot { width: 40px; height: 40px; border-radius: 50%; background: var(--brand-blue); }
  .brand-name {
    font-family: "Crimson Text", Georgia, serif; font-weight: 600;
    font-size: 46px; color: var(--brand-blue); line-height: 1;
  }
  .title {
    position: absolute; left: 466px; top: 150px;
    font-family: "Cinzel", "Times New Roman", serif; font-weight: 400;
    color: var(--white); font-size: 35px; letter-spacing: 1px; line-height: 1;
  }
  .subtitle {
    position: absolute; left: 466px; top: 195px;
    font-family: "Cinzel", "Times New Roman", serif;
    color: var(--pale-blue); font-size: 19px; letter-spacing: 1.2px; line-height: 1;
    white-space: nowrap;
  }
  .hero {
    position: absolute; left: 0; top: 242px; width: 100%; height: 418px;
    background: linear-gradient(110deg, #eef4f8 0%, #dbe7ef 35%, #f4efe9 65%, #ffffff 100%);
  }
  .hero-rule {
    position: absolute; left: 0; top: 660px; width: 100%; height: 8px;
    background: var(--brand-blue);
  }
  .badge { position: absolute; left: 12px; top: 450px; width: 210px; height: 210px; }
  .badge-text {
    position: absolute; left: 45px; top: 505px; width: 144px;
    text-align: center;
    font-family: "Crimson Text", Georgia, serif; font-style: italic;
    font-size: 20px; line-height: 24px; color: var(--sky-blue);
  }
  .column {
    position: absolute; top: 668px; height: 386px;
  }
  .mission { left: 0; width: 441px; padding: 26px 26px 0 54px; }
  .services {
    left: 441px; width: 434px; padding: 26px 38px 0 44px;
    background: var(--sky-blue);
    border-left: 2px solid var(--pale-blue);
  }
  .section-title {
    font-family: "Cinzel", "Times New Roman", serif; font-weight: 600;
    font-size: 19px; line-height: 24px; letter-spacing: 1px; color: var(--deep-blue);
    margin-bottom: 18px;
  }
  .mission p, .mission li {
    font-size: 14px; line-height: 18.5px; color: var(--body-text);
  }
  .beliefs { list-style: none; margin-top: 12px; }
  .beliefs li { color: var(--accent-blue); margin-bottom: 2px; }
  .services p {
    font-size: 13.5px; line-height: 18px; color: var(--deep-blue);
    text-align: justify;
  }
  .footer {
    position: absolute; left: 0; top: 1054px; width: 100%; height: 89px;
    background: var(--brand-blue);
    display: flex; justify-content: center; align-items: center; gap: 38px;
    padding-right: 70px;
    font-size: 20px; color: var(--footer-text);
  }
</style>
</head>
<body>
<main class="flyer">
  <header class="header">
    <svg class="header-curve" width="877" height="242" viewBox="0 0 877 242" aria-hidden="true">
      <path d="M0 0 H877 V14 Q520 150 0 126 Z" fill="#ffffff"/>
      <path d="M0 128 Q520 152 877 16" fill="none" stroke="#5cbde8" stroke-width="5"/>
    </svg>
    <div class="brand">
      <span class="brand-dot"></span>
      <span class="brand-name">Sunny Sprout</span>
    </div>
    <h1 class="title">SCHOOL HEALTH</h1>
    <p class="subtitle">SERVICES EXECUTIVE SUMMARY</p>
  </header>

  <div class="hero" role="img" aria-label="Photo of a smiling nurse with a stethoscope examining a young girl holding a teddy bear"></div>
  <div class="hero-rule"></div>

  <svg class="badge" viewBox="0 0 210 210" aria-hidden="true">
    <polygon fill="#0f5fae" points="105,2 116,24 133,6 138,30 159,16 157,41 181,34 172,57 197,57 183,78 206,86 186,101 206,116 184,126 197,147 172,148 180,172 156,166 158,191 137,178 132,203 116,186 105,208 94,186 78,203 73,178 52,191 54,166 30,172 38,148 13,147 26,126 4,116 24,101 4,86 27,78 13,57 38,57 29,34 53,41 51,16 72,30 77,6 94,24"/>
  </svg>
  <p class="badge-text">This service is also at NO out-of-pocket cost to the school</p>

  <section class="column mission">
    <h2 class="section-title">MISSION STATEMENT</h2>
    <p>SSI Larkfield Holdings, LLC, dba, "Sunny Sprout", feels a strong sense of connection to entities whose mission is to improve the educational achievements of students. In a similar way, Sunny Sprout is committed to improving the health of children by providing healthcare to students in a school-based setting. We work to keep children healthy, ready to learn and in the classroom.<br>We believe that:</p>
    <ul class="beliefs">
      <li>a)&nbsp; Undiagnosed and untreated health problems are barriers to a child's ability to learn.</li>
      <li>b)&nbsp; Preventive health services, provided in the school settings, reduce or eliminate barriers to healthcare.</li>
      <li>c)&nbsp; That diversity is to be valued and respected.</li>
    </ul>
  </section>

  <section class="column services">
    <h2 class="section-title">DESCRIPTION OF SERVICES</h2>
    <p>These annual screenings and sports physicals will comply with the Early Periodic Screening, Diagnosis and Treatment (EPSDT) as mandated by the Tennessee Medicaid program. The intent of our EPSDT program is to identify problems pre-K through 12th grade, to check health status at different intervals (Periodic), provide services that will identify health issues (Screening) that lead to classification of health issues (Diagnosis and follow-up), and elimination or provide ongoing care for behavioral diagnosed health problems (Treatment).<br>Sunny Sprout brings and sets up a well-equipped clinic to each school site. Our practitioners diagnose medical illnesses and make referrals to the child's primary care provider (PCP).</p>
  </section>

  <footer class="footer">
    <span>Tel;&nbsp; 615-555-0148</span>
    <span>schoolhealth@sunnysprout-kids.com</span>
  </footer>
</main>
</body>
</html>
```